Marketing material for IT Company
Brochure/Sales Sheet/Flyer
Brochure will be in two languages, and tri-fold. Would go like this; front (outer) side: first fold: page for information in 2nd languge, second fold: page for information in 2nd language, third fold: cover page in 1st language; back side (inner) side: first fold is for information in 1st language, second fold is for information in 1st language, third fold is cover page for 2nd language.
Information Technology
Brochure view and dimensions are in an uploaded file. Size of flyer equals to size of 1 fold of brochure (i.e one brochure size = 3 flyers size). Size of Sales Sheet is equal to brochure's size. (Sales Sheet won't be folded).
Trifold Brochure view and dimensions
Tulmori logo and Divisions logos (CMYK)
Tulmori logo and Divisions logos (PMS)
Tulmori vertical logo and Divisions vertical logos (CMYK)
Tulmori vertical logo and Divisions vertical logos (PMS)
Tulmori old Brochure (uploaded as an example)
Example of our folder, if it can help
Example of our biz card, if it can help
To help you understand how we see our brochure, one more PIC
Tulmori logo colors information

```html
<!DOCTYPE html>
<html lang="en">
<head>
<meta charset="utf-8">
<title>Tulmori Tri-fold Brochure</title>
<link href="https://fonts.googleapis.com/css2?family=Open+Sans:wght@400;600&family=Montserrat:wght@500&display=swap" rel="stylesheet">
<style>
  :root {
    --backdrop: #2b2724;
    --paper: #ffffff;
    --paper-dark: #3b3b3e;
    --ink: #6d6d6d;
    --ink-light: #c9c9c9;
    --brand: #34495a;
    --accent-blue: #1d6fb8;
    --stripe-red: #d6322e;
    --stripe-orange: #ef8a1f;
    --stripe-yellow: #f3c623;
    --stripe-green: #4fa84a;
    --stripe-blue: #2a7cc1;
    --stripe-purple: #7a3d93;
  }
  * { box-sizing: border-box; margin: 0; padding: 0; }
  html, body { width: 1200px; height: 901px; overflow: hidden; }
  body { background: var(--backdrop); font-family: "Open Sans", Arial, sans-serif; position: relative; }

  .spread { position: absolute; left: 195px; width: 815px; height: 396px; display: flex; box-shadow: 0 6px 18px rgba(0,0,0,.5); }
  .spread--outer { top: 29px; background: var(--paper); }
  .spread--inner { top: 482px; background: var(--paper-dark); }
  .panel { position: relative; width: 271.7px; height: 100%; overflow: hidden; }

  .mosaic-image { height: 198px; background: linear-gradient(135deg, #0d4f8f 0%, #2f86c9 35%, #9fcbea 65%, #ffffff 100%); }
  .office-image { background: radial-gradient(circle at 60% 45%, #7fb6e0 0%, #2f5f8c 40%, #14263c 100%); }

  .body-copy { font-size: 6.4px; line-height: 9.2px; color: var(--ink); text-align: justify; }
  .spread--inner .body-copy { color: var(--ink-light); }
  .body-copy p + p { margin-top: 8px; }

  .panel-text { padding: 14px 16px 0 16px; }
  .panel-footer { position: absolute; bottom: 6px; left: 16px; font-size: 5px; color: #999; }

  .middle-top { height: 120px; padding: 10px 16px 0; }
  .middle-photo { position: absolute; left: 0; right: 0; top: 120px; bottom: 0; }
  .inner-middle-photo { position: absolute; left: 0; right: 0; top: 118px; height: 160px; }
  .inner-middle-bottom { position: absolute; left: 16px; right: 16px; top: 290px; }

  .cover-brand { position: absolute; left: 0; right: 0; top: 150px; display: flex; flex-direction: column; align-items: center; gap: 10px; }
  .brand-dot { width: 44px; height: 44px; border-radius: 50%; background: var(--accent-blue); }
  .brand-name { font-family: "Montserrat", Arial, sans-serif; font-weight: 500; font-size: 34px; color: var(--brand); letter-spacing: .5px; }
  .spread--inner .brand-name { color: #e4e4e4; }

  .color-stripe { position: absolute; left: 0; right: 0; bottom: 18px; height: 6px; display: flex; }
  .color-stripe span { flex: 1; }

  .contact-block { position: absolute; left: 16px; right: 16px; bottom: 14px; display: flex; justify-content: space-between; font-size: 5.6px; line-height: 8.5px; color: var(--ink-light); }
  .contact-line { display: flex; align-items: center; gap: 3px; }
  .contact-line svg { width: 6px; height: 6px; }
</style>
</head>
<body>

<section class="spread spread--outer">
  <div class="panel">
    <div class="mosaic-image" role="img" aria-label="Blue tiled technology mosaic photo"></div>
    <div class="panel-text body-copy">
      <p>We plan, build and support secure systems for growing firms. Our teams handle networks, cloud services, data centres and software so your staff can focus on daily work. Every project starts with a clear audit, a fixed budget and a named engineer who stays with you from the first meeting to final handover and beyond.</p>
      <p>Our divisions cover hardware supply, licensing, managed support and training. Clients rely on fast response times, honest advice and long term care for every device on their network.</p>
    </div>
    <div class="panel-footer">www.lorvex.net</div>
  </div>

  <div class="panel">
    <div class="middle-top body-copy">
      <p>We plan, build and support secure systems for growing firms. Our teams handle networks, cloud services, data centres and software so your staff can focus on daily work. Every project starts with a clear audit, a fixed budget and a named engineer who stays with you from the first meeting to final handover and beyond.</p>
    </div>
    <div class="middle-photo office-image" role="img" aria-label="Photo of a businessman touching a glowing digital interface"></div>
  </div>

  <div class="panel">
    <div class="cover-brand">
      <div class="brand-dot"></div>
      <div class="brand-name">Tulmori</div>
    </div>
    <div class="color-stripe">
      <span style="background:var(--stripe-red)"></span>
      <span style="background:var(--stripe-orange)"></span>
      <span style="background:var(--stripe-yellow)"></span>
      <span style="background:var(--stripe-green)"></span>
      <span style="background:var(--stripe-blue)"></span>
      <span style="background:var(--stripe-purple)"></span>
    </div>
  </div>
</section>

<section class="spread spread--inner">
  <div class="panel">
    <div class="mosaic-image" role="img" aria-label="Blue tiled technology mosaic photo"></div>
    <div class="panel-text body-copy">
      <p>We plan, build and support secure systems for growing firms. Our teams handle networks, cloud services, data centres and software so your staff can focus on daily work. Every project starts with a clear audit, a fixed budget and a named engineer who stays with you from the first meeting to final handover and beyond.</p>
      <p>Our divisions cover hardware supply, licensing, managed support and training. Clients rely on fast response times, honest advice and long term care for every device on their network.</p>
    </div>
    <div class="panel-footer">www.lorvex.net</div>
  </div>

  <div class="panel">
    <div class="middle-top body-copy">
      <p>We plan, build and support secure systems for growing firms. Our teams handle networks, cloud services, data centres and software so your staff can focus on daily work. Every project starts with a clear audit, a fixed budget and a named engineer who stays with you from the first meeting to final handover and beyond.</p>
    </div>
    <div class="inner-middle-photo office-image" role="img" aria-label="Photo of a businessman touching a glowing digital interface"></div>
    <div class="inner-middle-bottom body-copy">
      <p>Our divisions cover hardware supply, licensing, managed support and training. Clients rely on fast response times, honest advice and long term care for every device on their network.</p>
    </div>
  </div>

  <div class="panel">
    <div class="cover-brand">
      <div class="brand-dot"></div>
      <div class="brand-name">Tulmori</div>
    </div>
    <div class="contact-block">
      <div>
        <div>Tulmori Center, Suite 4</div>
        <div>12 Harbor Lane</div>
        <div>PO Box 880</div>
        <div>Eastport 1010</div>
      </div>
      <div>
        <div class="contact-line"><svg viewBox="0 0 10 10"><path d="M2 1h2l1 2-1 1a6 6 0 0 0 2 2l1-1 2 1v2a1 1 0 0 1-1 1A8 8 0 0 1 1 2a1 1 0 0 1 1-1z" fill="#c9c9c9"/></svg>+000 12 555 0101</div>
        <div class="contact-line"><svg viewBox="0 0 10 10"><path d="M2 1h2l1 2-1 1a6 6 0 0 0 2 2l1-1 2 1v2a1 1 0 0 1-1 1A8 8 0 0 1 1 2a1 1 0 0 1 1-1z" fill="#c9c9c9"/></svg>+000 12 555 0102</div>
        <div class="contact-line"><svg viewBox="0 0 10 10"><rect x="1" y="2" width="8" height="6" fill="none" stroke="#c9c9c9"/><path d="M1 2l4 3 4-3" fill="none" stroke="#c9c9c9"/></svg>info@lorvex.net</div>
        <div class="contact-line"><svg viewBox="0 0 10 10"><circle cx="5" cy="5" r="4" fill="none" stroke="#c9c9c9"/></svg>www.lorvex.net</div>
      </div>
    </div>
  </div>
</section>

</body>
</html>
```